Brindle Advisory Business Card Design

Business card for business consulting company, using attached logo. We do financial and strategic consulting, and want a clean, professional image with a bit of fun. Our logo is a flat whale tail, which symbolizes the Orca whale, a highly collaborative, group based animal that is very successful in navigating the ocean, protecting the herd, and hunting. We like the logo that is blue and gray on white one one side, but would be open to a blue card with white lettering on the other side... or whatever you'd suggest
Updates
Hi all - I have had the logo modified to take the shadowing off the tail. I will post it on the brief... under a file name called updated logo. thank you Added Saturday, April 25, 2015
Target Market(s)
Small to medium sized businesses ($10M to $500M in revenue per year), financial and sales executives, general managers, attorneys and CPAs
Industry/Entity Type
Financial
Contact Information for Business Card
Want company name, contact info - name, title, telephone, email, website, linkedin, twitter and Facebook. No physical address yet.
Requirements
Must have
- contemporary design, bold, strong, confident but with a bit of fun. prominently feature the logo and the whale tail icon
Nice to have
- unique touches that would differentiate us from a regular card... for example, logo and writing all on front on white background, but on back - logo in white on a blue background
- open to idea of different shapes of card than standard... but not sure
Should not have
- ?

```html
<!DOCTYPE html>
<html lang="en">
<head>
<meta charset="utf-8">
<title>Brindle Advisory – Business Card</title>
<link rel="stylesheet" href="https://fonts.googleapis.com/css2?family=Open+Sans:wght@400;600;700&display=swap">
<style>
  :root {
    --backdrop: #9b9b9b;
    --card-white: #ffffff;
    --navy: #17375f;
    --navy-icon: #1e3a66;
    --grey-text: #9a9a9a;
    --rule: #555a60;
  }
  * { margin: 0; padding: 0; box-sizing: border-box; }
  html, body {
    width: 1200px;
    height: 900px;
    overflow: hidden;
    background: var(--backdrop);
    font-family: "Open Sans", Arial, sans-serif;
  }
  .stage {
    position: relative;
    width: 1200px;
    height: 900px;
  }
  .card {
    position: absolute;
    left: 285px;
    width: 629px;
    height: 360px;
  }
  .card-front { top: 74px; background: var(--card-white); }
  .card-back { top: 465px; background: var(--navy); overflow: hidden; }

  .holder-name {
    position: absolute;
    right: 59px;
    top: 137px;
    font-size: 22px;
    font-weight: 700;
    color: var(--navy-icon);
    letter-spacing: 0.5px;
  }
  .name-rule {
    position: absolute;
    left: 50px;
    right: 59px;
    top: 166px;
    height: 1px;
    background: linear-gradient(to right, rgba(85,90,96,0), var(--rule) 40%, var(--rule));
  }
  .holder-title {
    position: absolute;
    right: 56px;
    top: 171px;
    font-size: 13px;
    font-weight: 600;
    color: var(--grey-text);
    letter-spacing: 3px;
  }
  .contact-list {
    position: absolute;
    left: 47px;
    top: 200px;
    list-style: none;
  }
  .contact-item {
    display: flex;
    align-items: center;
    height: 25.5px;
    font-size: 13px;
    color: var(--grey-text);
  }
  .contact-icon {
    width: 18px;
    height: 18px;
    margin-right: 8px;
    flex: none;
  }
  .social-square {
    width: 17px;
    height: 17px;
    margin-right: 9px;
    background: var(--navy-icon);
    border-radius: 2px;
    flex: none;
  }

  .company-name {
    position: absolute;
    left: 0;
    right: 0;
    top: 158px;
    text-align: center;
    font-size: 30px;
    font-weight: 700;
    color: var(--card-white);
  }
  .back-url {
    position: absolute;
    left: 0;
    right: 0;
    top: 327px;
    text-align: center;
    font-size: 13px;
    color: var(--card-white);
    letter-spacing: 5px;
  }
</style>
</head>
<body>
<main class="stage">
  <section class="card card-front">
    <div class="holder-name">XXXXXXX</div>
    <div class="name-rule"></div>
    <div class="holder-title">PRESIDENT</div>
    <ul class="contact-list">
      <li class="contact-item">
        <svg class="contact-icon" viewBox="0 0 24 24" aria-hidden="true"><path fill="#1e3a66" d="M6.6 10.8c1.4 2.8 3.8 5.1 6.6 6.6l2.2-2.2c.3-.3.7-.4 1-.2 1.1.4 2.3.6 3.6.6.6 0 1 .4 1 1V20c0 .6-.4 1-1 1C10.6 21 3 13.4 3 4c0-.6.4-1 1-1h3.5c.6 0 1 .4 1 1 0 1.3.2 2.5.6 3.6.1.3 0 .7-.2 1z"/></svg>
        <span>xxx xxx xxxx</span>
      </li>
      <li class="contact-item">
        <span class="social-square"></span>
        <span>xxx xxx xxxx</span>
      </li>
      <li class="contact-item">
        <svg class="contact-icon" viewBox="0 0 24 24" aria-hidden="true"><rect x="2" y="5" width="20" height="14" fill="#1e3a66"/><path d="M2 5l10 8 10-8" fill="none" stroke="#fff" stroke-width="1.5"/></svg>
        <span>xxxxx@xxxxxx.com</span>
      </li>
      <li class="contact-item">
        <svg class="contact-icon" viewBox="0 0 24 24" aria-hidden="true"><g fill="none" stroke="#1e3a66" stroke-width="1.8"><circle cx="12" cy="12" r="9.5"/><ellipse cx="12" cy="12" rx="4" ry="9.5"/><path d="M2.5 12h19M4 7h16M4 17h16"/></g></svg>
        <span>www.xxxxxxxx.com</span>
      </li>
      <li class="contact-item">
        <span class="social-square"></span>
        <span>xxx xxx xxxx</span>
      </li>
    </ul>
  </section>

  <section class="card card-back">
    <div class="company-name">Brindle Advisory</div>
    <div class="back-url">www.xxxxxxxx.com</div>
  </section>
</main>
</body>
</html>
```